Organic, Vegan friendly and luxurious face moisturiser branding needed

Hi team

We are in the process of launching an all organic, no nasties facial moisturiser that will suite both men and woman.
We have narrowed down the bottle packaging and box packaging but need to clarify the dimensions, however we are happy to start with a few concepts. We need artwork for both the bottle and box to be designed.

The bottle will be a gloss white finish with a white dispensing pump on top. We would like to keep the colour scheme as clean as possible as the final design will be printed directly onto the bottle.
We would like to keep all text and artwork black however we are happy to explore a few shades of darker grey in the design as well.

Overall the message we want to convey through the art is one of Luxury, Pinnacle brand, eco friendliness and Organic.

Attached is a few images of artwork we like, the bottle shape will be near identical.

The brand name will be : Vendra, which means Honest in Norwegian.
We would like the tagline "Uncomplicated Skincare" to be shown somewhere on the bottle.

Ideally the front design will show the name : Vendra - Organics
Tagline "uncomplicated skincare"
Facial Moisturiser
Some sort of picture depicting the ingredients, we like floral/botanical inspiration such as some of the images attached - Ideally we want some of our ingredients to shine one the front - Some of them include:

1. Organic Aloe
2. Organic Shea
3. Green tea
4. Organic Jojoba

At the bottom front of the bottle we you will also need to display the content size, which will be 100ml/ 3.3 FL OZ

At the back the list of ingredients needs to be shown.

Aloe Barbadensis Leaf Juice (Organic Aloe), Aqua (Water), Helianthus Annuus Seed Oil (Organic Sunflower), Isopropyl Palmitate, Glyceryl Stearate SE, Cetyl Alcohol, Stearic Acid, Glycerin ( Kosher Vegetable), Butyrospermum Parkii Butter (Organic Shea), Simmondsia Chinesis Seed Oil (Organic Jojoba), Panthenol (Vitamin B5), Tocopherol Acetate (Vitamin E), Camelia Sinensis Leaf Extract (Green Tea), Xanthane Gum, Phenoxyethanol, Ethylhexylglycerin..

Alongside this we want to list the following:

1. The product is Vegan friendly
2. No Animal Testing
3 .Kosher Certified
4. Sustainable Raw Materials
5. Powered with 100% Renewable Wind Energy
6. Certified organic

You can design little logos instead of writing it out.

Hi Everyone. Please use the following template for the information on the back of the bottle. Vendra How to use: Apply twice a day to face and throat all over, or where needed. For best results, thoroughly wash face prior to use. Ingredients: Aloe Barbadensis Leaf Juice (Organic Aloe), Aqua (Water), Helianthus Annuus Seed Oil (Organic Sunflower), Isopropyl Palmitate (Plant based), Glyceryl Stearate SE (Plant based), Cetyl Alcohol (Plant based), Stearic Acid (Plant based), Glycerin ( Kosher Vegetable), Butyrospermum Parkii Butter (Organic Shea), Simmondsia Chinesis Seed Oil (Organic Jojoba), Panthenol (Vitamin B5), Tocopherol Acetate (Vitamin E), Camelia Sinensis Leaf Extract (Green Tea),  Xanthan Gum (Plant based), Phenoxyethanol (Natural preservative), Ethylhexylglycerin (Plant based) Caution: For External use only. Avoid contact with eyes. If contact occurs, rinse thoroughly with water. Keep out of reach of children. This delightful lotion absorbs right into the skin without leaving a greasy feeling yet provides the glide of a deep penetrating moisturizer. It conditions your skin while it moisturizes and softens and will leave your skin glowing. Vendra Organics info@vendracosmetics.example Made in the USA

Industry/Entity Type

Cosmetics

Font styles to use
Serif
Sans Serif

Colors
5c5c5c
333333
000000
ffffff

Requirements
Must have
• Attached is the example of the clean bottle.
• Here are the dimensions of the bottle :
• Single Specs:
• White/White/White
• Weight: 39.67g
• Width: 47.48mm
• Height: 124.90mm
• Airless Bottle, White Cap, White Pump and Collar, White Body, 100mL

```html
<!DOCTYPE html>
<html lang="en">
<head>
<meta charset="utf-8">
<title>Vendra Organics – Facial Moisturizer Label</title>
<link rel="stylesheet" href="https://fonts.googleapis.com/css2?family=Bebas+Neue&family=Poppins:wght@600&family=Raleway:wght@400&family=Open+Sans:wght@400&display=swap">
<style>
  :root {
    --label-white: #ffffff;
    --ink-black: #000000;
    --ink-charcoal: #333333;
    --ink-grey: #5c5c5c;
    --leaf-light: #ececec;
    --leaf-mid: #bdbdbd;
  }
  * { margin: 0; padding: 0; box-sizing: border-box; }
  html, body {
    width: 900px;
    height: 1200px;
    overflow: hidden;
    background: var(--label-white);
  }
  .label {
    position: relative;
    width: 900px;
    height: 1200px;
    background: var(--label-white);
  }
  .brand {
    position: absolute;
    top: 250px;
    left: 0;
    width: 100%;
    text-align: center;
    font-family: "Poppins", sans-serif;
    font-weight: 600;
    color: var(--ink-charcoal);
  }
  .brand-name {
    display: block;
    font-size: 78px;
    line-height: 1;
    letter-spacing: -2px;
  }
  .brand-line {
    display: block;
    margin-top: 4px;
    font-size: 13px;
    letter-spacing: 7px;
  }
  .botanical-art {
    position: absolute;
    top: 420px;
    left: 300px;
    width: 300px;
    height: 330px;
  }
  .product-name {
    position: absolute;
    top: 790px;
    left: 0;
    width: 100%;
    text-align: center;
    font-family: "Bebas Neue", sans-serif;
    font-size: 74px;
    letter-spacing: 1px;
    color: var(--ink-charcoal);
    line-height: 1;
  }
  .tagline {
    position: absolute;
    top: 880px;
    left: 0;
    width: 100%;
    text-align: center;
    font-family: "Raleway", sans-serif;
    font-size: 15px;
    letter-spacing: 5px;
    color: var(--ink-grey);
    text-transform: uppercase;
  }
  .content-size {
    position: absolute;
    top: 950px;
    right: 190px;
    font-family: "Open Sans", sans-serif;
    font-size: 18px;
    color: var(--ink-charcoal);
  }
</style>
</head>
<body>
  <main class="label">
    <div class="brand">
      <span class="brand-name">vendra</span>
      <span class="brand-line">ORGANICS</span>
    </div>

    <svg class="botanical-art" viewBox="0 0 300 330" role="img" aria-label="Line-drawn illustration of two ginkgo-style botanical leaves on long stems">
      <defs>
        <radialGradient id="leafTone" cx="55%" cy="35%" r="65%">
          <stop offset="0%" stop-color="var(--leaf-mid)"/>
          <stop offset="100%" stop-color="var(--leaf-light)"/>
        </radialGradient>
      </defs>
      <rect x="0" y="0" width="300" height="330" rx="12" fill="url(#leafTone)"/>
    </svg>

    <h1 class="product-name">Facial Moisturizer</h1>
    <p class="tagline">Uncomplicated&nbsp; Skincare</p>
    <p class="content-size">100ml/ 3.3 FL OZ</p>
  </main>
</body>
</html>
```